Italian restaurant needs a flyer to promote wine tasting and wine pairing tours

Need a designer to create one flyer for print and digital use.

(3 pages all either postcard or 1/3 page)Intro page, wine tasting and wine pairing page, wine pairing and cruise page

We are Www.lunaverdetrattoria.com an top rated Italian restaurant in CABO San Lucas mexico. Our info and history is on the website. We are a fun, cozy bistro ambience that makes you feel like you are in Italy.

Get to know the great tastes of Rome right here in CABO San Lucas at Corvale Bistro. Farm and sea to table and select national and international wines . We begin with a brief introduction of the restaurant including a quick Salute to the kitchen then sit at our reserved table for a fun and tasty wine food pairing.

Our Founding Chef and In House Sommelier join forces to create four fabulous farm and sea to table dishes, using the freshest ingredients from local sources and only the top wines from small vineyards. Guests are guided through four wine & food pairings, with a some fun facts about wine and the wine producing regions of Mexico. A lively resort casual setting and a night you will never forget.

Wine & Dine Pairing Session includes:
* Welcome cocktail!
* 4-Course Wine Pairing menu
* Each course paired with local wines
* After Tasting Night cap
* Regional history, Wine tasting tips, trivia, and prizes!
* Guests receive 20% off their next reservation
* Everyday at 5:30pm and 9:30pm for one hour and 45 minutes.
* Limited to 10 guests per session please reserve in advance.
* 69usd X person. Tax included .

Target Market(s)

Wine lovers coming to CABO San Lucas

Industry/Entity Type

Restaurant

Font styles to use
Serif

Requirements
Must have
• More image and less text with an elegant yet fun setting
• Must have wine and dine description:
• Get to know the great tastes of Rome right here in CABO San Lucas at Corvale Bistro. Farm and sea to table and select national and international wines . We begin with a brief introduction of the restaurant including a quick Salute to the kitchen then sit at our reserved table for a fun and tasty wine food pairing.
• Our Founding Chef and In House Sommelier join forces to create four fabulous farm and sea to table dishes, using the freshest ingredients from local sources and only the top wines from small vineyards. Guests are guided through four wine & food pairings, with a some fun facts about wine and the wine producing regions of Mexico. A lively resort casual setting and a night you will never forget.
• Wine & Dine Pairing Session includes:
• * Welcome cocktail!
• * 4-Course Wine Pairing menu
• * Each course paired with local wines
• * After Tasting Night cap
• * Regional history, Wine tasting tips, trivia, and prizes!
• * Guests receive 20% off their next reservation
• * Everyday at 5:30pm and 9:30pm for one hour and 45 minutes.
• * Limited to 10 guests per session please reserve in advance.
• * 69usd X person. Tax included .
• amd must have wine tasting description:
• One hour of fun and flavor!
• Join our in house sommelier in this small group, one hour , lively happy hour party that includes ample tastes of 3 fine wines paired with authentic Italian gourmet appetizers and seasonal menu favorites. Let us share the best of Bajas wines amd perfectly paired tasting menu before hitting the town.
• This Wine Tasting Happy hour includes:
• * Welcome cocktail!
• * 4-Course Tasting menu
• * Each course paired with Baja local wines
• * Starts at 5pm or 6pm. Arrive 5 minutes prior for check in. Space is limited to 20 guests so advanced reservations are recommended.
• * 25usd per person tax included.
• Colors should be like our website www.lunaverdetrattoria.com
• Files must be editable
Nice to have
• Want this to focus on promoting the restaurant and tours
Should not have
• Errors

```html
<!DOCTYPE html>
<html lang="en">
<head>
<meta charset="utf-8">
<title>Corvale Bistro – Wine Tasting Trifold</title>
<link href="https://fonts.googleapis.com/css2?family=Cinzel:wght@500&family=Dancing+Script:wght@700&family=Lato:ital,wght@0,400;1,400&family=Oswald:wght@500&display=swap" rel="stylesheet">
<style>
  :root{
    --bg:#d4d4d8;
    --wine-dark:#4a0e0c;
    --wine:#6e1b14;
    --wine-warm:#8a3a22;
    --wood:#5a2a16;
    --wood-light:#7d4325;
    --gold:#e2b93b;
    --yellow:#f6d31c;
    --cream:#f3e9dc;
    --ink:#2a0a07;
    --placeholder:#d9d4cc;
  }
  *{box-sizing:border-box;margin:0;padding:0}
  html,body{width:1200px;height:1200px;overflow:hidden;background:var(--bg)}
  .brochure{position:absolute;left:90px;top:75px;width:1020px;height:1050px;display:flex;box-shadow:0 20px 40px rgba(0,0,0,.25)}
  .panel{position:relative;width:340px;height:100%;overflow:hidden;color:var(--cream);
    background:linear-gradient(180deg,var(--wine-warm) 0%,var(--wine) 45%,var(--wine-dark) 100%)}
  .panel + .panel{border-left:1px solid rgba(0,0,0,.25)}

  .brand{text-align:center;font-family:"Cinzel",serif;font-weight:500;color:var(--gold);line-height:1}
  .brand-name{font-size:34px;letter-spacing:2px}
  .brand-sub{font-size:16px;letter-spacing:3px;margin-top:4px}
  .brand-rule{width:200px;margin:10px auto 6px;border-top:2px dashed var(--gold)}
  .brand-tag{font-family:"Cinzel",serif;font-size:12px;letter-spacing:1px;color:var(--gold);text-align:center}
  .web{position:absolute;bottom:26px;left:0;right:0;text-align:center;font-family:"Lato",sans-serif;font-size:12px;letter-spacing:4px;color:var(--cream)}

  .pour-photo{height:450px;background:radial-gradient(ellipse at 40% 40%,#c98a7a 0%,#8a3a2a 45%,var(--wine-warm) 80%)}
  .desc-title{font-family:"Dancing Script",cursive;font-weight:700;color:var(--yellow);font-size:28px;text-align:center;margin:30px 0 20px}
  .desc{padding:0 32px;font-family:"Lato",sans-serif;font-style:italic;font-size:12.5px;line-height:1.55;text-align:justify}
  .desc p + p{margin-top:14px}

  .contact{background:linear-gradient(180deg,#7a1f16,#5a1410)}
  .map{width:250px;height:250px;margin:170px auto 0;border-radius:50%;border:9px solid var(--yellow);background:var(--placeholder)}
  .contact .brand{margin-top:70px}
  .contact .brand-name{font-size:28px}
  .contact .brand-sub{font-size:13px}
  .contact .brand-rule{width:170px}
  .contact-line{text-align:center;font-family:"Lato",sans-serif;margin-top:22px}
  .contact-line svg{display:block;margin:0 auto 6px}
  .phone{font-size:26px;letter-spacing:1px}
  .address{font-size:12.5px;line-height:1.35}
  .listing-badge{position:absolute;bottom:40px;left:50%;transform:translateX(-50%);width:70px;height:70px;border-radius:50%;border:4px solid var(--cream)}

  .cover .brand{margin-top:40px}
  .headline{font-family:"Dancing Script",cursive;font-weight:700;font-size:48px;line-height:1.05;text-align:center;color:#fff;margin-top:40px}
  .still-life{position:absolute;left:0;right:0;top:560px;height:300px;
    background:radial-gradient(ellipse at 50% 70%,#5b2436 0%,#3a1420 35%,transparent 70%),linear-gradient(180deg,transparent,rgba(0,0,0,.25))}
  .offer{position:absolute;right:22px;top:640px;width:110px;height:110px;border-radius:50%;background:var(--yellow);color:var(--ink);
    display:flex;flex-direction:column;justify-content:center;align-items:center;font-family:"Oswald",sans-serif;line-height:1.05}
  .offer b{font-size:22px;font-weight:500}
  .offer span{font-family:"Lato",sans-serif;font-size:15px}
  .offer small{font-family:"Lato",sans-serif;font-size:11px}
  .table{position:absolute;left:0;right:0;bottom:0;height:190px;
    background:repeating-linear-gradient(90deg,var(--wood) 0 36px,var(--wood-light) 36px 38px,var(--wood) 38px 70px)}
  .table::before{content:"";position:absolute;left:0;right:0;top:0;height:16px;background:var(--wood-light)}
  .schedule{position:absolute;left:0;right:0;bottom:74px;text-align:center;font-family:"Oswald",sans-serif;font-weight:500;font-size:14px;letter-spacing:.5px;line-height:1.5;text-transform:uppercase}
</style>
</head>
<body>
<main class="brochure">

  <section class="panel story">
    <div class="pour-photo" role="img" aria-label="Red wine being poured into a glass"></div>
    <h2 class="desc-title">Wine and dine description</h2>
    <div class="desc">
      <p>Get to know the great tastes of Rome right here in CABO San Lucas at Corvale Bistro. Farm and sea to table and select national and international wines. We begin with a brief introduction of the restaurant including a quick Salute to the kitchen then sit at our reserved table for a fun and tasty wine food pairing.</p>
      <p>Our Founding Chef and In House Sommelier join forces to create four fabulous farm and sea to table dishes, using the freshest ingredients from local sources and only the top wines from small vineyards. Guests are guided through four wine &amp; food pairings, with some fun facts about wine and the wine producing regions of Mexico. A lively resort casual setting and a night you will never forget.</p>
    </div>
    <p class="web">www.lunaverdetrattoria.com</p>
  </section>

  <section class="panel contact">
    <div class="map" role="img" aria-label="Location map of the restaurant in Cabo San Lucas"></div>
    <div class="brand">
      <div class="brand-name">CORVALE</div>
      <div class="brand-sub">BISTRO</div>
    </div>
    <div class="brand-rule"></div>
    <p class="brand-tag">MEDITERRANEAN CUISINE</p>
    <div class="contact-line">
      <svg width="22" height="20" viewBox="0 0 24 22" fill="var(--yellow)"><path d="M2 8c0-4 5-6 10-6s10 2 10 6v2h-5V8c-2-1-8-1-10 0v2H2z"/><path d="M6 12h12l2 8H4z"/><circle cx="12" cy="16" r="2" fill="var(--wine)"/></svg>
      <p class="phone">555 0192</p>
    </div>
    <div class="contact-line" style="margin-top:8px">
      <svg width="22" height="20" viewBox="0 0 24 22" fill="var(--yellow)"><path d="M12 1l11 10h-3v10h-6v-6h-4v6H4V11H1z"/></svg>
      <p class="address">Calle Olivo 14, Centro<br>Cabo San Lucas, Mexico</p>
    </div>
    <div class="listing-badge" aria-hidden="true"></div>
  </section>

  <section class="panel cover">
    <div class="brand">
      <div class="brand-name">CORVALE</div>
      <div class="brand-sub">BISTRO</div>
    </div>
    <div class="brand-rule"></div>
    <p class="brand-tag">MEDITERRANEAN CUISINE</p>
    <h1 class="headline">Wine tasting<br>and<br>Wine Pairing<br>tours</h1>
    <div class="still-life" role="img" aria-label="Bottle of red wine, a filled glass and a bunch of red grapes on a wooden board"></div>
    <div class="offer"><b>20% OFF</b><span>their next</span><small>reservation</small></div>
    <div class="table"></div>
    <p class="schedule">Everyday at 5:30pm and 9:30pm<br>for one hour and 45 minutes</p>
    <p class="web">www.lunaverdetrattoria.com</p>
  </section>

</main>
</body>
</html>
```